Business Card And Stationary Set for : Pintu Ravel Sdn. Bhd.
I need double sided standard sized Business Card [3.5" x 2"]
Same font or you can recommend
Professional
Ferril Wakin
41C, Jalan Cempaka Lima,
Taman Seroja,
47310 Kuala Lumpur,
Malaysia.
info@pintuvrel.com.my
www.pintuvrel.com.my
618204-K
Please put the company name and license no. above the company address. Smaller font for the license number.
Pintu Ravel Sdn. Bhd. (618204-K)
Company logo.
Specialized In: Auto Gate & Security Systems

```html
<!DOCTYPE html>
<html lang="en">
<head>
<meta charset="utf-8">
<title>Pintu Ravel Business Card</title>
<link href="https://fonts.googleapis.com/css2?family=Source+Sans+3:wght@400;600;700&display=swap" rel="stylesheet">
<style>
  :root {
    --backdrop: #4a2516;
    --orange-light: #ff9a1f;
    --orange-deep: #f07a0c;
    --charcoal: #2a2a2a;
    --graphite: #4c4c4c;
    --ink: #1f1f1f;
    --white: #ffffff;
    --accent: #ff8c1a;
    --rule: #bdbdbd;
  }
  * { margin: 0; padding: 0; box-sizing: border-box; }
  html, body { width: 1200px; height: 965px; overflow: hidden; }
  body {
    background: var(--backdrop);
    font-family: "Source Sans 3", "Myriad Pro", sans-serif;
    position: relative;
  }
  .card {
    position: absolute;
    left: 240px; top: 235px;
    width: 777px; height: 439px;
    border-radius: 20px;
    overflow: hidden;
    background: radial-gradient(ellipse 60% 70% at 50% 45%, var(--graphite), var(--charcoal) 75%, #1c1c1c);
  }
  .contact-band {
    position: absolute;
    left: 0; top: 0; right: 0;
    height: 172px;
    background: linear-gradient(180deg, var(--orange-light), var(--orange-deep));
    border-bottom: 3px solid var(--rule);
  }
  .divider {
    position: absolute;
    left: 400px; top: 20px;
    width: 2px; height: 132px;
    background: var(--ink);
  }
  .address {
    position: absolute;
    right: 399px; top: 20px;
    text-align: right;
    color: var(--ink);
    font-size: 17px;
    line-height: 26px;
  }
  .address .company { font-weight: 700; }
  .address .license { font-weight: 400; font-size: 13px; }
  .contacts {
    position: absolute;
    left: 428px; top: 26px;
    list-style: none;
    color: var(--ink);
    font-size: 17px;
    line-height: 30px;
  }
  .contacts li { display: flex; align-items: center; gap: 12px; }
  .contacts .icon { width: 20px; height: 20px; display: flex; align-items: center; justify-content: center; font-weight: 700; }
  .brand {
    position: absolute;
    left: 60px; top: 330px;
    display: flex; align-items: center; gap: 14px;
  }
  .brand-mark {
    width: 30px; height: 30px;
    background: var(--accent);
  }
  .brand-name {
    color: var(--white);
    font-weight: 700;
    font-size: 42px;
    line-height: 1;
    letter-spacing: 1px;
  }
  .holder-name {
    position: absolute;
    left: 520px; top: 305px;
    color: var(--accent);
    font-weight: 600;
    font-size: 25px;
  }
</style>
</head>
<body>
  <article class="card">
    <section class="contact-band">
      <div class="address">
        <div><span class="company">Pintu Ravel Sdn. Bhd.</span> <span class="license">(618204-K)</span></div>
        <div>41C, Jalan Cempaka Lima,</div>
        <div>Taman Seroja,</div>
        <div>47310 Kuala Lumpur,</div>
        <div>Malaysia.</div>
      </div>
      <div class="divider"></div>
      <ul class="contacts">
        <li><span class="icon"><svg width="18" height="18" viewBox="0 0 24 24"><path fill="#1f1f1f" d="M6.6 10.8c1.4 2.8 3.8 5.1 6.6 6.6l2.2-2.2c.3-.3.7-.4 1-.2 1.1.4 2.3.6 3.6.6.6 0 1 .4 1 1V20c0 .6-.4 1-1 1C10.6 21 3 13.4 3 4c0-.6.4-1 1-1h3.5c.6 0 1 .4 1 1 0 1.3.2 2.5.6 3.6.1.3 0 .7-.2 1z"/></svg></span>+603 5521 4406</li>
        <li><span class="icon"><svg width="14" height="20" viewBox="0 0 14 20"><rect x="1" y="1" width="12" height="18" rx="2" fill="none" stroke="#1f1f1f" stroke-width="2"/><rect x="4" y="4" width="6" height="6" fill="#1f1f1f"/><circle cx="7" cy="15" r="1.5" fill="#1f1f1f"/></svg></span>+6012 4470 318</li>
        <li><span class="icon"><svg width="18" height="18" viewBox="0 0 18 18"><rect x="4" y="1" width="10" height="6" fill="#1f1f1f"/><rect x="1" y="7" width="16" height="10" rx="1" fill="#1f1f1f"/><rect x="4" y="10" width="10" height="1.5" fill="#ff9a1f"/><rect x="4" y="13" width="10" height="1.5" fill="#ff9a1f"/></svg></span>+603 5521 4407</li>
        <li><span class="icon">@</span>info@pintuvrel.com.my</li>
      </ul>
    </section>
    <div class="brand">
      <span class="brand-mark"></span>
      <span class="brand-name">PINTU RAVEL</span>
    </div>
    <div class="holder-name">Ferril Wakin</div>
  </article>
</body>
</html>
```